Maple Syrup Bottle (front) Label design

I need label design for a 16fl OZ rectangular bottle of maple syrup with the usable dimensions of: Front: 4" x 2" and the back area for "ingredient specifications" of: 6" x 2". The maple syrup product comes from our own farm and is a quality product. The technical name/class of the syrup is: Grade A / AMBER
Updates

I can’t seem to find a way to upload a photo of the maple syrup bottle, but the front dimensions are clearly written on bottle description. Again: 4.5” by 2.25”

I have tried to upload the photo of the maple syrup bottle several times, and it seems (from my side) that it is successful. But I can never find it and the artists cannot find it either. Not sure what to do.

I have tried several times to add a photo of maple bottle, but it never shows up

This seems to be a futile exercise

I would like to post some images of the actual cedar Hollow (not the one on Quorvo, though!
But I can’t get back to the page that allows that to happen. Please advise!

Somebody PLEASE ask PV management to make it possible for me to upload more images! The "add photos" etc. just disappears from anywhere.

Target Market(s)

High-end food stores

Industry/Entity Type

Maple syrup retail industry

Font styles to use
Other font styles liked:
• I don't know, and welcome suggestions

Colors

Designer to choose colors to be used in the design.

Requirements
Must have
• Name of Farm: Cedar Hollow Maple
Nice to have
• The label can be "minimalist" and elegant. There is already a Maple leaf glass relief on the top of front of the bottle.
Should not have
• and NOT include farm buildings with steam coming out the chimney, etc.

```html
<!DOCTYPE html>
<html lang="en">
<head>
<meta charset="utf-8">
<title>Cedar Hollow Maple – Syrup Label</title>
<link rel="stylesheet" href="https://fonts.googleapis.com/css2?family=Rammetto+One&family=Oranienbaum&family=Archivo:wght@700&display=swap">
<style>
  :root {
    --bg: #0d0d0f;
    --label-deep: #5a0a08;
    --label-mid: #9c1712;
    --label-glow: #c0281a;
    --relief: #b3231a;
    --gold: #f4a23a;
    --gold-soft: #e8983a;
    --tree: #d9822e;
    --ink: #111111;
    --paper: #ffffff;
  }
  * { margin: 0; padding: 0; box-sizing: border-box; }
  html, body {
    width: 1200px; height: 848px; overflow: hidden;
    background: var(--bg);
  }
  .canvas {
    position: relative; width: 1200px; height: 848px;
    display: flex; justify-content: center; align-items: center; gap: 60px;
  }
  .label {
    position: relative; width: 280px; height: 700px;
    border-radius: 6px;
    background: radial-gradient(ellipse at 50% 45%, var(--label-glow) 0%, var(--label-mid) 45%, var(--label-deep) 100%);
    display: flex; flex-direction: column; align-items: center;
    color: var(--gold);
  }
  .relief {
    width: 150px; height: 190px; margin-top: 40px;
    border-radius: 45% 45% 40% 40%;
    background: radial-gradient(ellipse at 50% 45%, var(--relief) 0%, rgba(179,35,26,0) 70%);
  }
  .brand {
    display: flex; flex-direction: column; align-items: center; gap: 14px;
    margin-top: 30px;
  }
  .label--back .brand { margin-top: 60px; }
  .brand-dot {
    width: 48px; height: 48px; border-radius: 50%;
    border: 5px solid var(--gold);
  }
  .brand-name {
    font-family: "Rammetto One", sans-serif;
    font-size: 34px; line-height: 1.1; text-align: center;
    color: var(--gold);
  }
  .label--back .brand-name { font-size: 30px; }
  .claim {
    display: flex; align-items: center; gap: 10px;
    margin-top: 34px;
  }
  .claim-text {
    font-family: "Rammetto One", sans-serif;
    font-size: 24px; line-height: 1.25; text-align: center;
    color: var(--gold-soft);
  }
  .label--back .claim { margin-top: 28px; }
  .label--back .claim-text { font-size: 19px; }
  .tree {
    width: 26px; height: 44px; margin-top: 24px;
    border-radius: 50% 50% 10% 10%;
    background: linear-gradient(180deg, var(--tree), #8a3d14);
  }
  .label--back .tree { width: 22px; height: 38px; margin-top: 20px; }
  .volume {
    margin-top: auto; margin-bottom: 56px;
    font-family: "Oranienbaum", serif;
    font-size: 34px; color: var(--gold-soft);
  }
  .ingredients {
    margin-top: 28px; text-align: center;
    font-family: "Oranienbaum", serif; color: var(--gold-soft);
  }
  .ingredients h2 { font-weight: 400; font-size: 34px; margin-bottom: 4px; }
  .ingredients p { font-size: 23px; line-height: 1.45; }
  .barcode-box {
    margin-top: auto; margin-bottom: 50px;
    width: 200px; height: 136px;
    background: var(--paper);
    display: flex; align-items: center; justify-content: center;
    font-family: "Archivo", sans-serif; font-weight: 700;
    font-size: 15px; color: var(--ink);
  }
</style>
</head>
<body>
<main class="canvas">
  <section class="label label--front">
    <div class="relief" role="img" aria-label="Maple leaf glass relief on the bottle"></div>
    <div class="brand">
      <span class="brand-dot"></span>
      <div class="brand-name">Cedar Hollow<br>Maple</div>
    </div>
    <div class="claim">
      <div class="tree" role="img" aria-label="Small maple tree illustration"></div>
      <div class="claim-text">PREMIUM<br>PURE<br>100%</div>
      <div class="tree" role="img" aria-label="Small maple tree illustration"></div>
    </div>
    <div class="volume">~ 16fl Oz ~</div>
  </section>

  <section class="label label--back">
    <div class="brand">
      <span class="brand-dot"></span>
      <div class="brand-name">Cedar Hollow<br>Maple</div>
    </div>
    <div class="claim">
      <div class="tree" role="img" aria-label="Small maple tree illustration"></div>
      <div class="claim-text">PREMIUM<br>PURE<br>100%</div>
      <div class="tree" role="img" aria-label="Small maple tree illustration"></div>
    </div>
    <div class="ingredients">
      <h2>Ingredients:</h2>
      <p>Pure maple syrup<br>Sourced in</p>
    </div>
    <div class="barcode-box">BARCODE HERE</div>
  </section>
</main>
</body>
</html>
```